Charitable and Benefit Event Auctioneer and Emcee

My name is Wes
People know me as Wes The Auctioneer
My email is westheauctioneer@...
Include Phone number
This is a very unique and distinct type of Auctioneering that focuses on high profile charitable events including black tie galas, fundraisers and golf tournaments...
Clients include hospitals, schools, service agencies, corporations, foundations
Event consultation is also offered
Graduate of The Brightwater Valley School of Auctioneering
in the Fundraising Auction business since 1998

Reason: I have been too busy to give time to appropriate time to the designs submitted and I'm still having learning challenges with the pixelguild website.

Target Market(s)

Very high profile nonprofit organizations hosting gala events raising millions of dollars.

Industry/Entity Type

Events

Font styles to use
Sans Serif

Colors

Designer to choose colors to be used in the design.

Requirements
Must have
• Classy, eye catching, unique.

```html
<!DOCTYPE html>
<html lang="en">
<head>
<meta charset="utf-8">
<title>Wes The Auctioneer – Business Card</title>
<link rel="stylesheet" href="https://fonts.googleapis.com/css2?family=Fira+Sans+Condensed:wght@400;500&display=swap">
<style>
  :root {
    --backdrop: #d6d6d6;
    --card-charcoal: #2b2b2b;
    --brand-red: #a3080d;
    --ink-white: #f2f2f2;
    --ink-soft: #dcdcdc;
  }
  html, body {
    margin: 0;
    padding: 0;
    width: 1200px;
    height: 741px;
    overflow: hidden;
    background: var(--backdrop);
  }
  .stage {
    position: relative;
    width: 1200px;
    height: 741px;
  }
  .business-card {
    position: absolute;
    left: 75px;
    top: 70px;
    width: 1050px;
    height: 600px;
    background: var(--card-charcoal);
    box-shadow: 0 10px 30px rgba(0,0,0,0.25);
    font-family: "Fira Sans Condensed", sans-serif;
    color: var(--ink-white);
    overflow: hidden;
  }
  .brand-band {
    position: absolute;
    left: 84px;
    top: 0;
    width: 306px;
    height: 100%;
    background: var(--brand-red);
  }
  .brand-name {
    position: absolute;
    left: 22px;
    top: 20px;
    margin: 0;
    font-size: 138px;
    font-weight: 400;
    line-height: 1;
    letter-spacing: -2px;
  }
  .brand-title {
    position: absolute;
    left: 24px;
    top: 178px;
    margin: 0;
    font-weight: 400;
    line-height: 0.95;
  }
  .brand-title .article {
    display: block;
    font-size: 46px;
  }
  .brand-title .role {
    display: block;
    font-size: 52px;
    letter-spacing: 0.5px;
  }
  .service-list {
    position: absolute;
    left: 412px;
    top: 168px;
    margin: 0;
    padding: 0;
    list-style: none;
    font-size: 33px;
    font-weight: 400;
    line-height: 1.05;
    letter-spacing: 1.5px;
    text-transform: uppercase;
    color: var(--ink-soft);
  }
  .contact-line {
    position: absolute;
    left: 412px;
    display: flex;
    align-items: center;
    gap: 18px;
    font-size: 31px;
    color: var(--ink-soft);
  }
  .contact-line svg { width: 28px; height: 28px; fill: var(--brand-red); }
  .contact-email { top: 262px; }
  .contact-phone { top: 336px; }
</style>
</head>
<body>
<main class="stage">
  <article class="business-card">
    <div class="brand-band">
      <h1 class="brand-name">Wes</h1>
      <p class="brand-title"><span class="article">the</span><span class="role">AUCTIONEER</span></p>
    </div>
    <ul class="service-list">
      <li>High Profile Auctioneering</li>
      <li>Events Consultation</li>
    </ul>
    <div class="contact-line contact-email">
      <svg viewBox="0 0 24 24" aria-hidden="true"><path d="M2 7l10 6 10-6v11H2z M2 5h20l-10 6z"/></svg>
      <span>westheauctioneer@brightmail.com</span>
    </div>
    <div class="contact-line contact-phone">
      <svg viewBox="0 0 24 24" aria-hidden="true"><path d="M6.6 10.8a15.1 15.1 0 0 0 6.6 6.6l2.2-2.2c.3-.3.7-.4 1-.2 1.1.4 2.3.6 3.6.6.6 0 1 .4 1 1V20c0 .6-.4 1-1 1A17 17 0 0 1 3 4c0-.6.4-1 1-1h3.5c.6 0 1 .4 1 1 0 1.3.2 2.5.6 3.6.1.3 0 .7-.2 1z"/></svg>
      <span>555 0142 0198</span>
    </div>
  </article>
</main>
</body>
</html>
```